Agricultural Consulting Website

Provide a modern yet business like website for my new Agriculture Consulting Business in Australia called FenTrove. Whilst we are based in Australia we are targetting both domestic and international markets (especially in Asia). We are targetting corporate, small business, government and farmer clients. The design should compliment our logo also sourced through pixel guild. The webiste should be easy for me to keep updated on a regular basis without the need to go back to the designer.

Industry/Entity Type

Business

Requirements
Must have
• clean crisp feel
• be modern yet business like
• be able to be updated by myself easily

```html
<!DOCTYPE html>
<html lang="en">
<head>
<meta charset="utf-8">
<title>FenTrove – Agricultural Consulting</title>
<link rel="stylesheet" href="https://fonts.googleapis.com/css2?family=Ubuntu:wght@300;400;500&display=swap">
<style>
  :root {
    --brown: #663300;
    --brown-dark: #4e2a08;
    --green: #5f9311;
    --panel: #5e5140;
    --text: #2b2b2b;
    --muted: #555;
    --footer: #e8e8e8;
    --badge: #b9b9b9;
    --white: #ffffff;
  }
  * { box-sizing: border-box; margin: 0; padding: 0; }
  html, body { width: 1200px; height: 836px; overflow: hidden; }
  body { font-family: "Ubuntu", sans-serif; color: var(--text); }
  .stage { position: relative; width: 1200px; height: 836px; overflow: hidden; }
  .backdrop {
    position: absolute; inset: 0;
    background:
      linear-gradient(90deg, rgba(70,120,40,.55) 0%, rgba(0,0,0,0) 40%, rgba(0,0,0,0) 70%, rgba(200,150,50,.6) 100%),
      linear-gradient(180deg, #4f86cc 0%, #8db6e4 30%, #d5e4f2 50%, #7fa24a 60%, #6b8a35 80%, #8c7a3a 100%);
  }
  .page { position: absolute; left: 175px; top: 22px; width: 850px; height: 769px; background: var(--white); }
  .header { position: absolute; left: 0; top: 0; width: 850px; height: 96px;
    background: linear-gradient(180deg, #ffffff 0%, #efefef 100%); }
  .brand { position: absolute; left: 16px; top: 21px; display: flex; align-items: center; gap: 10px; }
  .brand-mark { width: 54px; height: 54px; background: var(--green); }
  .brand-name { font-size: 40px; font-weight: 400; color: var(--brown-dark); letter-spacing: -0.5px; }
  .call { position: absolute; right: 17px; top: 40px; font-size: 19px; font-weight: 300; color: var(--green); }
  .call strong { font-weight: 400; color: var(--brown-dark); }
  .nav { position: absolute; left: 0; top: 96px; width: 850px; height: 32px; background: var(--brown); }
  .nav a { position: absolute; top: 0; height: 32px; line-height: 33px; font-size: 14px; color: var(--white); text-decoration: none; }
  .nav .active { left: 16px; width: 76px; background: var(--green); text-align: center; }
  .slider { position: absolute; left: 14px; top: 140px; width: 820px; height: 278px; border: 1px solid #c9c9c9; background: var(--white); }
  .slide-photo { position: absolute; left: 4px; top: 3px; width: 518px; height: 270px;
    background: radial-gradient(ellipse at 50% 40%, #9a8a6a 0%, #6e5e48 45%, #4c4032 100%); }
  .slide-panel { position: absolute; left: 522px; top: 3px; width: 288px; height: 270px; background: var(--panel); color: var(--white); }
  .slide-panel h2 { position: absolute; left: 7px; top: 43px; font-size: 28px; font-weight: 400; }
  .slide-panel p { position: absolute; left: 11px; top: 87px; width: 262px; font-size: 15px; font-weight: 300; line-height: 20.6px; letter-spacing: -0.2px; }
  .learn { position: absolute; left: 9px; top: 201px; height: 27px; padding: 0 4px; background: var(--green);
    font-size: 15px; line-height: 28px; font-weight: 300; color: var(--white); }
  .dots { position: absolute; left: 249px; top: 250px; display: flex; gap: 4px; }
  .dots span { width: 8px; height: 8px; background: #9b9080; }
  .dots span:first-child { background: var(--white); }
  .welcome { position: absolute; left: 15px; top: 438px; width: 502px; }
  .welcome h1 { font-size: 23px; font-weight: 300; color: var(--text); margin-bottom: 6px; }
  .welcome p { font-size: 13px; font-weight: 300; line-height: 18.8px; color: var(--text); margin-bottom: 9px; letter-spacing: -0.25px; }
  .divider { position: absolute; left: 541px; top: 437px; height: 182px; border-left: 1px dotted #c8c8c8; }
  .services { position: absolute; left: 567px; top: 443px; }
  .services h3 { font-size: 18px; font-weight: 300; margin-bottom: 6px; }
  .services li { list-style: none; font-size: 13px; font-weight: 300; line-height: 22.5px; color: var(--muted); padding-left: 2px; letter-spacing: -0.25px; }
  .badges { position: absolute; left: 0; top: 658px; width: 850px; height: 44px; }
  .badge { position: absolute; top: 0; height: 44px; background: var(--badge); }
  .footer { position: absolute; left: 0; top: 739px; width: 850px; height: 30px; background: var(--footer);
    font-size: 13px; font-weight: 300; line-height: 32px; color: #111; letter-spacing: -0.2px; }
  .footer .copy { position: absolute; left: 15px; }
  .footer .links { position: absolute; right: 17px; }
</style>
</head>
<body>
<div class="stage">
  <div class="backdrop" role="img" aria-label="Blue sky with clouds above green and golden wheat fields"></div>
  <div class="page">
    <header class="header">
      <div class="brand"><span class="brand-mark"></span><span class="brand-name">FenTrove</span></div>
      <div class="call">Call Now: <strong>+11 555 210 3086</strong></div>
    </header>
    <nav class="nav">
      <a class="active" href="#">Home</a>
      <a href="#" style="left:124px">About Us</a>
      <a href="#" style="left:224px">Our Services</a>
      <a href="#" style="left:345px">Our Clients</a>
      <a href="#" style="left:458px">Contact Us</a>
    </nav>
    <section class="slider">
      <div class="slide-photo" role="img" aria-label="Hands cupped around a young seedling growing in soil"></div>
      <div class="slide-panel">
        <h2>We Help you Grow</h2>
        <p>Lorem Ipsum is simply dummy text of the printing and typesetting industry. Lorem Ipsum has been the industry's standard dummy text ever since the 1500s.</p>
        <span class="learn">LEARN MORE</span>
        <div class="dots"><span></span><span></span><span></span></div>
      </div>
    </section>
    <section class="welcome">
      <h1>Welcome to Our Website</h1>
      <p>Lorem Ipsum is simply dummy text of the printing and typesetting industry. Lorem Ipsum has been the industry's standard dummy text ever since the 1500s, when an unknown printer took a galley of type and scrambled it to make a type specimen book. It has survived not only five centuries, but also the leap into electronic typesetting, remaining essentially unchanged.</p>
      <p>It was popularised in the 1960s with the release of Typeline sheets containing Lorem Ipsum passages, and more recently with desktop publishing software like Quillset Layout including versions of Lorem Ipsum.</p>
    </section>
    <div class="divider"></div>
    <aside class="services">
      <h3>Our Services</h3>
      <ul>
        <li>- Financial matters</li>
        <li>- Business structure</li>
        <li>- Human relations and Personnel management</li>
        <li>- Business succession planning</li>
        <li>- Production</li>
        <li>- Evolving technologies</li>
      </ul>
    </aside>
    <div class="badges" aria-label="Accreditation badges">
      <span class="badge" style="left:15px;width:87px"></span>
      <span class="badge" style="left:170px;width:104px"></span>
      <span class="badge" style="left:328px;width:60px;border-radius:50%"></span>
      <span class="badge" style="left:463px;width:44px;border-radius:50%"></span>
      <span class="badge" style="left:589px;width:39px"></span>
      <span class="badge" style="left:713px;width:117px"></span>
    </div>
    <footer class="footer">
      <span class="copy">Copyright © 2013 FenTrove | All Rights Reserved</span>
      <span class="links">Home | About Us | Our Services | Our Clients | Contact Us</span>
    </footer>
  </div>
</div>
</body>
</html>
```